QRV MOONLIT GLOW Party

Hi,
Want to design a flyer for a party.

I have attached a design I would like you to work from and just add in the correct text:

QRV Events presents

November 2013

MOONLIT GLOW
PARTY

DJ COPPER LANTERN
VENUE: TBA

DOORS OPEN 8PM

ENTRY STRICTLY OVER 18'S.

DRESS CODE: SMART CASUAL SULTRY SEXY SPRING THREADS

COST: $60 PER HEAD, includes champagne, beer & wine and canapes.

Tickets from www.quietrivervista.com.au or 0491 570 156.

```html
<!DOCTYPE html>
<html lang="en">
<head>
<meta charset="utf-8">
<title>QRV Moonlit Glow Party</title>
<link href="https://fonts.googleapis.com/css2?family=Montserrat:ital,wght@0,300;0,400;0,500;0,600;1,400&family=Syncopate:wght@400;700&family=Michroma&display=swap" rel="stylesheet">
<style>
  :root {
    --ink: #060606;
    --silver-hi: #f4f4f4;
    --silver-mid: #a9abae;
    --silver-lo: #5b5d60;
    --gold: #f2c230;
    --gold-deep: #c8911a;
    --white: #ffffff;
    --soft-white: #e8e8e8;
    --rule: #8c8c8c;
  }
  * { margin: 0; padding: 0; box-sizing: border-box; }
  html, body { width: 703px; height: 1200px; overflow: hidden; background: var(--ink); }
  .flyer {
    position: relative;
    width: 703px;
    height: 1200px;
    overflow: hidden;
    background: radial-gradient(ellipse at 50% 45%, #1c1c20 0%, var(--ink) 70%);
    font-family: "Montserrat", sans-serif;
    color: var(--white);
  }
  .frame-top, .frame-bottom {
    position: absolute; left: 0; width: 100%;
    background: linear-gradient(180deg, var(--silver-hi), var(--silver-mid) 50%, var(--silver-lo));
  }
  .frame-top { top: 0; height: 20px; }
  .frame-bottom { bottom: 0; height: 18px; }
  .frame-side {
    position: absolute; top: 20px; bottom: 18px; width: 5px;
    background: linear-gradient(90deg, var(--silver-lo), var(--silver-mid), var(--silver-lo));
  }
  .frame-side.left { left: 0; }
  .frame-side.right { right: 0; }
  .tufted-header {
    position: absolute; top: 20px; left: 5px; right: 5px; height: 60px;
    background: linear-gradient(180deg, #2a2a2e, #0b0b0c);
  }
  .vip-ribbon { position: absolute; top: 0; right: 0; width: 150px; height: 110px; }
  .line {
    position: absolute; left: 0; width: 100%; text-align: center; white-space: nowrap;
    text-transform: uppercase;
  }
  .presenter { top: 97px; font-size: 18px; font-weight: 500; letter-spacing: 2px; }
  .presenter-rule {
    position: absolute; top: 132px; left: 230px; width: 243px; height: 2px;
    background: linear-gradient(90deg, transparent, var(--white), transparent);
  }
  .event-date {
    top: 150px; font-family: "Michroma", sans-serif; font-size: 30px; letter-spacing: 1px;
    background: linear-gradient(180deg, #ffe27a, var(--gold) 50%, var(--gold-deep));
    -webkit-background-clip: text; background-clip: text; color: transparent;
  }
  .event-date sup { font-size: 16px; vertical-align: 14px; }
  .hero-art {
    position: absolute; top: 195px; left: 36px; width: 631px; height: 640px;
    background: radial-gradient(ellipse at 50% 40%, #d9dde3 0%, #8fa3b8 22%, #2d3440 48%, transparent 72%);
  }
  .title-pastel {
    position: absolute; top: 720px; left: 115px; font-family: "Michroma", sans-serif;
    font-size: 14px; letter-spacing: 1px; color: var(--soft-white);
  }
  .title-main, .title-sub {
    font-family: "Syncopate", sans-serif;
    background: linear-gradient(180deg, #ffffff 0%, #e0e0e0 45%, #7b7d80 55%, #d6d6d6 100%);
    -webkit-background-clip: text; background-clip: text; color: transparent;
  }
  .title-main { top: 738px; font-size: 70px; font-weight: 700; letter-spacing: -2px; }
  .title-sub { top: 822px; font-size: 56px; font-weight: 400; letter-spacing: -1px; }
  .party-label { top: 932px; font-size: 18px; color: var(--gold); letter-spacing: 1px; }
  .rule { position: absolute; left: 144px; width: 446px; height: 1px; background: var(--rule); }
  .rule.first { top: 958px; }
  .rule.second { top: 1030px; }
  .detail { font-size: 19px; font-weight: 300; letter-spacing: 0.5px; }
  .detail b { font-weight: 500; }
  .dj { top: 968px; }
  .venue { top: 1002px; }
  .doors { top: 1037px; font-size: 15px; color: var(--gold); }
  .inclusions { top: 1057px; font-size: 13px; font-style: italic; color: var(--gold); }
  .dresscode { top: 1077px; font-size: 15px; color: var(--gold); }
  .footer-band {
    position: absolute; left: 0; top: 1104px; width: 100%; height: 78px;
    background: var(--ink);
    border-top: 5px solid var(--silver-mid);
  }
  .tickets { top: 1115px; font-size: 15px; font-weight: 500; }
  .tickets b { font-weight: 600; letter-spacing: 2px; }
  .charity-note {
    position: absolute; top: 1138px; left: 84px; width: 560px;
    font-size: 12.5px; letter-spacing: 0.5px; line-height: 16px; text-transform: uppercase;
  }
  .charity-badge {
    position: absolute; top: 1128px; left: 22px; width: 44px; height: 46px;
    background: #2b2b2b; border: 1px solid var(--silver-mid);
  }
</style>
</head>
<body>
<main class="flyer">
  <div class="tufted-header"></div>
  <div class="frame-top"></div>
  <div class="frame-side left"></div>
  <div class="frame-side right"></div>
  <div class="frame-bottom"></div>

  <svg class="vip-ribbon" viewBox="0 0 150 110">
    <polygon points="40,0 90,0 150,60 150,110" fill="#050505"/>
    <line x1="40" y1="0" x2="150" y2="110" stroke="#c8911a" stroke-width="1.5"/>
    <line x1="90" y1="0" x2="150" y2="60" stroke="#c8911a" stroke-width="1.5"/>
    <text x="104" y="40" fill="#f2c230" font-family="Montserrat, sans-serif" font-size="12" font-weight="600" transform="rotate(45 104 40)">VIP</text>
  </svg>

  <p class="line presenter">QRV &nbsp;Events presents</p>
  <div class="presenter-rule"></div>
  <p class="line event-date">November 9<sup>th</sup> 2013</p>

  <div class="hero-art" role="img" aria-label="Party artwork: woman in a white halter gown crouching before a mirror ball, gold champagne bottles, microphones, speakers, white doves and dark wings"></div>

  <p class="title-pastel">PASTEL</p>
  <h1 class="line title-main">MOONLIT</h1>
  <h2 class="line title-sub">GLOW</h2>

  <p class="line party-label">Party</p>
  <div class="rule first"></div>
  <p class="line detail dj">Dancefloor: <b>DJ COPPER LANTERN</b></p>
  <p class="line detail venue">Venue: <b>TBA</b></p>
  <div class="rule second"></div>
  <p class="line doors">Doors open 8 PM &nbsp;| &nbsp;Tickets: $60 per head &nbsp;| &nbsp;Entry strictly over 18's</p>
  <p class="line inclusions">(Includes champagne, beer &amp; wine and canapes)</p>
  <p class="line dresscode">Dress code: Smart casual sultry sexy spring threads</p>

  <div class="footer-band"></div>
  <div class="charity-badge"></div>
  <p class="line tickets">Tickets: <b>0491 570 156</b> or www.quietrivervista.com.au</p>
  <p class="charity-note">Donations and all profits made on the night go to skin cancer research.</p>
</main>
</body>
</html>
```